Spa Business Card Design Project

Hello! We are a boutique spa for men and women that is rebranding. I would like a memorable new business card that showcases our beautiful new logo and our unique business. I would like it to be classic/timeless and eclectic/artistic at the  same time.
I am a fan of negative space as you can tell from the logo. I am also open to any creative ideas.
Multi sided design. Two sided design is acceptable as an option, too. "Flaps/folds/whatever the design term is" are optional- whether full vertical or horizontal, half flap, full flap etc
On either side next to the golden snail I would potentially like to see "breathe in. take time."  Possibly on one statment on top of each other, crowned with the snail. Or the statment following the snail on one line... I am open for a creative suprise, too.
The back I would like room for the standard Information
"3817 Birch Lane
Ashford, New York 12731
(518) 462 3085
info@thecorvella spa.com
The snail is to be done in gold ink.
Can I also Have an option for cards that are individualized for staff members, too?

Updates
Project Deadline Extended
Reason: I apologize for the deadline extension. My day was more involved than anticipated in other matters. Hope to have this closed by next Tuesday.
Thank you

Target Market(s)
Men and women with expendable income between the ages of 30-55
Industry/Entity Type
Boutique
Requirements
Must have
- only black and gold ink.

Nice to have
- One of a kind.
Showcase the snail :-)
make you smile :-)
Fun, but professional.
Should not have
- Lots of color.
Too feminine.
Too busy.

```html
<!DOCTYPE html>
<html lang="en">
<head>
<meta charset="utf-8">
<title>The Corvella Spa — Business Card</title>
<link href="https://fonts.googleapis.com/css2?family=Raleway:wght@300;400;500;600&display=swap" rel="stylesheet">
<style>
  :root {
    --backdrop: #e9e7e3;
    --card-white: #ffffff;
    --card-dark: #2b2624;
    --gold: #c99a3e;
    --gold-soft: #d7b067;
    --ink: #2a2a2a;
    --ink-soft: #6b6b6b;
  }
  * { margin: 0; padding: 0; box-sizing: border-box; }
  html, body {
    width: 900px; height: 1200px; overflow: hidden;
    background: var(--backdrop);
    font-family: "Raleway", Arial, sans-serif;
  }
  .canvas {
    position: relative; width: 900px; height: 1200px;
    display: flex; flex-direction: column; align-items: center; justify-content: center; gap: 70px;
  }
  .card {
    position: relative; width: 700px; height: 400px;
    box-shadow: 0 10px 30px rgba(0,0,0,0.18);
  }
  .card__frame {
    position: absolute; inset: 22px;
    border: 1.5px solid var(--gold);
  }
  .card--front { background: var(--card-white); }
  .card--back { background: var(--card-dark); }

  .front__content {
    position: absolute; inset: 0;
    display: flex; flex-direction: column; align-items: center; text-align: center;
    padding-top: 58px;
  }
  .brand-name {
    display: flex; align-items: center; gap: 14px;
    font-size: 40px; font-weight: 600; letter-spacing: 3px; color: var(--ink);
    text-transform: uppercase;
  }
  .brand-name__dot {
    width: 16px; height: 16px; border-radius: 50%; background: var(--gold);
  }
  .brand-tagline {
    margin-top: 8px; font-size: 14px; color: var(--ink); letter-spacing: 0.5px;
  }
  .staff-name {
    margin-top: 44px; font-size: 28px; font-weight: 400; color: var(--gold);
  }
  .staff-role {
    margin-top: 2px; font-size: 15px; color: var(--ink); font-weight: 500;
  }
  .contact {
    margin-top: 22px; font-size: 13px; color: var(--ink-soft); line-height: 1.6;
  }
  .contact__sep { color: var(--gold); margin: 0 6px; }
  .contact__label { color: var(--gold); font-weight: 600; }
  .contact__web { color: var(--gold); }

  .back__content {
    position: absolute; inset: 0;
    display: flex; flex-direction: column; align-items: center; justify-content: center;
  }
  .emblem {
    width: 92px; height: 92px; border-radius: 50%; background: var(--gold);
  }
  .motto {
    margin-top: 30px; font-size: 24px; font-weight: 500; color: var(--gold-soft); letter-spacing: 0.5px;
  }
</style>
</head>
<body>
  <main class="canvas">
    <section class="card card--front" aria-label="Business card front">
      <div class="card__frame"></div>
      <div class="front__content">
        <div class="brand-name"><span class="brand-name__dot"></span>The Corvella Spa</div>
        <p class="brand-tagline">a boutique spa for Men &amp; Women</p>
        <p class="staff-name">Name Here</p>
        <p class="staff-role">Beauty therapist</p>
        <div class="contact">
          <p>3817 Birch Lane, Ashford, New York 12731</p>
          <p><span class="contact__label">T</span> (518) 462 3085<span class="contact__sep">|</span><span class="contact__label">E</span> info@thecorvella spa.com</p>
          <p class="contact__web">www.thecorvellaspa.com</p>
        </div>
      </div>
    </section>

    <section class="card card--back" aria-label="Business card back">
      <div class="card__frame"></div>
      <div class="back__content">
        <div class="emblem" role="img" aria-label="Gold spa emblem"></div>
        <p class="motto">breathe in. take time.</p>
      </div>
    </section>
  </main>
</body>
</html>
```